Web tool bar Project

I'm open to paying more if the quality of the bar is very good... if you feel the scope of the project does not match budget..... please quote me.

I need someone to re-design my web tool bar.

In the first attachment you can see a black tool bar (fig1). This is my old design. I want this to be the template as it shows what the text will say and where the buttons will be placed.

For the new tool bar:
-I would like the it to be white in colour (like fig.2)
-I would like the buttons to also be white. But the buttons must stand out so the designer should use the right shading to make the buttons stand out.
-The bar needs to be the quality of the bar in fig.2 (very good quality). I have had many designs done for this but no designer seems to be good enough to get the right quality.
-The text in the white boxes on the new bar should be the colours shown above the buttons next to fig.1 (blue, green, red, yellow, purple & orange).

Finally please put the logo attached (QT) at the end of the bar on the right where it says logo. The logo should blend in well with the bar as it has white in it also.

Please take note of fig.2 it is good quality with sharp edges I would like the same quality.

Any further questions please ask?

Requirements
Must have
• Quality!

```html
<!DOCTYPE html>
<html lang="en">
<head>
<meta charset="utf-8">
<title>Quiet Terrace Toolbar</title>
<link rel="stylesheet" href="https://fonts.googleapis.com/css2?family=Arimo:wght@400;700&display=swap">
<style>
  :root {
    --page: #fdfdfd;
    --bar-top: #ffffff;
    --bar-bottom: #ececec;
    --bar-line: #c9c9c9;
    --btn-top: #ffffff;
    --btn-bottom: #eeeeee;
    --btn-border: #bdbdbd;
    --icon: #555555;
    --divider: #d0d0d0;
    --blue: #0a86d2;
    --red: #d8121c;
    --yellow: #f2a900;
    --purple: #c50fc8;
    --orange: #f07a00;
    --logo-bg: #3a3a3a;
    --logo-text: #ffffff;
  }
  * { box-sizing: border-box; margin: 0; padding: 0; }
  html, body {
    width: 1200px; height: 229px; overflow: hidden;
    background: var(--page);
    font-family: "Arimo", Arial, sans-serif;
  }
  .toolbar {
    position: absolute; left: 0; top: 103px;
    width: 1200px; height: 40px;
    background: linear-gradient(var(--bar-top), var(--bar-bottom));
    border-top: 1px solid var(--bar-line);
    border-bottom: 1px solid var(--bar-line);
  }
  .btn {
    position: absolute; top: 7px; height: 25px;
    display: flex; align-items: center;
    background: linear-gradient(var(--btn-top), var(--btn-bottom));
    border: 1px solid var(--btn-border);
    border-radius: 4px;
    box-shadow: 0 1px 1px rgba(0,0,0,.12), inset 0 1px 0 #fff;
    font-size: 11px; white-space: nowrap;
  }
  .btn-item { display: flex; align-items: center; gap: 6px; padding: 0 7px; height: 100%; }
  .btn-item + .btn-item { border-left: 1px solid var(--divider); }
  .btn svg { flex: none; }
  .login { left: 25px; width: 126px; color: var(--blue); }
  .login .btn-item { padding-left: 5px; gap: 4px; }
  .group { left: 590px; width: 260px; }
  .checkin { color: var(--red); padding-left: 8px; gap: 7px; }
  .friends { color: var(--red); gap: 5px; }
  .feeds { left: 857px; width: 105px; color: var(--yellow); }
  .message { left: 968px; width: 80px; color: var(--purple); }
  .scrapbook { left: 1054px; width: 87px; color: var(--orange); }
  .brand {
    position: absolute; left: 1147px; top: 8px;
    width: 24px; height: 23px; border-radius: 3px;
    background: var(--logo-bg); color: var(--logo-text);
    font-size: 10px; font-weight: 700;
    display: flex; align-items: center; justify-content: center;
  }
</style>
</head>
<body>
  <div class="toolbar">
    <div class="btn login">
      <span class="btn-item">
        <svg width="10" height="17" viewBox="0 0 10 17"><circle cx="5" cy="4" r="3.6" fill="var(--icon)"/><rect x="3.8" y="6" width="2.4" height="10" fill="var(--icon)"/><rect x="6" y="12" width="2" height="1.6" fill="var(--icon)"/></svg>
        Quiet Terrace Login
      </span>
    </div>

    <div class="btn group">
      <span class="btn-item checkin">
        <svg width="19" height="15" viewBox="0 0 19 15"><rect x="0.5" y="1.5" width="17" height="13" fill="#fff" stroke="#8a8a8a"/><path d="M4 8 L8 11.5 L17 1" fill="none" stroke="var(--icon)" stroke-width="1.6"/></svg>
        Check - In
      </span>
      <span class="btn-item friends">
        <svg width="16" height="16" viewBox="0 0 16 16"><circle cx="6" cy="5" r="3" fill="#aaa"/><circle cx="9" cy="5.5" r="3.2" fill="var(--icon)"/><path d="M2 16 C2 10 16 10 16 16 Z" fill="var(--icon)"/></svg>
        Online Friends at Circlenet
      </span>
    </div>

    <div class="btn feeds">
      <span class="btn-item">
        <svg width="16" height="16" viewBox="0 0 16 16"><circle cx="3" cy="13" r="2" fill="#999"/><path d="M1 7 A8 8 0 0 1 9 15" fill="none" stroke="#999" stroke-width="2"/><path d="M1 2 A13 13 0 0 1 14 15" fill="none" stroke="#999" stroke-width="2"/></svg>
        Terrace Feeds
      </span>
    </div>

    <div class="btn message">
      <span class="btn-item">
        <svg width="16" height="11" viewBox="0 0 16 11"><rect x="0.5" y="0.5" width="15" height="10" fill="#fff" stroke="var(--icon)"/><path d="M0.5 0.5 L8 6 L15.5 0.5" fill="none" stroke="var(--icon)"/></svg>
        Message
      </span>
    </div>

    <div class="btn scrapbook">
      <span class="btn-item">
        <svg width="13" height="16" viewBox="0 0 13 16"><path d="M0.5 0.5 H9 L12.5 4 V15.5 H0.5 Z" fill="#fff" stroke="var(--icon)"/><path d="M3 6 H10 M3 8.5 H10 M3 11 H10 M3 13 H8" stroke="var(--icon)"/></svg>
        Scrapbook
      </span>
    </div>

    <div class="brand">QT</div>
  </div>
</body>
</html>
```